Crest of Morning Paddocks Business Cards with logo

Need a creative business card that pops. Colorful but professional. The attached logo should be included. We are a national horse racing partnership so we are in the equine business. Nothing cartoonlike or whimsical.

Target Market(s)

professionals - 40+

Contact Information for Business Card

Maren Dunleavy
Director of Operations
27 Ashbrook Lane
Middletown, MD. 21584

Phone (313) 555-0147

FX: (949) 555-0192

email: maren@cmpaddocks.example
cmpaddocks.example

Requirements
Must have
• All information above should be on the business card including the website address. Professional yet creative
Nice to have
• an attention grabbing design. not boring. exciting.
Should not have
• cartoon like - whimsical.

```html
<!DOCTYPE html>
<html lang="en">
<head>
<meta charset="utf-8">
<title>Crest of Morning Paddocks – Business Cards</title>
<link href="https://fonts.googleapis.com/css2?family=Merriweather:wght@400;700&display=swap" rel="stylesheet">
<style>
  :root {
    --navy: #2c2a7f;
    --gold: #b8902b;
    --ink: #1d1d24;
    --paper: #ffffff;
    --backdrop: #ececec;
  }
  * { box-sizing: border-box; margin: 0; padding: 0; }
  html, body {
    width: 1200px; height: 800px; overflow: hidden;
    background: var(--backdrop);
    font-family: "Merriweather", Georgia, serif;
  }
  .sheet {
    position: relative; width: 1200px; height: 800px;
    display: flex; align-items: center; justify-content: center; gap: 40px;
  }
  .card {
    position: relative; width: 520px; height: 298px;
    background: var(--paper);
    box-shadow: 0 1px 3px rgba(0,0,0,0.12);
    color: var(--ink);
    overflow: hidden;
  }
  .card--navy { --accent: var(--navy); }
  .card--gold { --accent: var(--gold); }

  .brand {
    position: absolute; left: 18px; top: 54px; width: 190px; height: 190px;
    display: flex; flex-direction: column; align-items: center; justify-content: center;
    text-align: center;
  }
  .brand__dot {
    width: 22px; height: 22px; border-radius: 50%;
    background: var(--gold); margin-bottom: 12px;
  }
  .brand__name {
    color: var(--navy); font-weight: 700; font-size: 17px; line-height: 1.3;
  }

  .divider {
    position: absolute; left: 226px; top: 50px; width: 2px; height: 198px;
    background: var(--accent);
  }

  .contact {
    position: absolute; left: 246px; top: 48px;
    font-size: 14.5px; line-height: 22px;
    white-space: nowrap;
  }
  .contact__name { color: var(--accent); font-weight: 700; font-size: 17px; line-height: 22px; }
  .contact__role { margin-bottom: 12px; }
  .contact__address { margin-bottom: 10px; }
  .contact__label { color: var(--accent); }
</style>
</head>
<body>
<main class="sheet">
  <article class="card card--navy">
    <div class="brand">
      <span class="brand__dot"></span>
      <p class="brand__name">Crest of<br>Morning<br>Paddocks</p>
    </div>
    <span class="divider"></span>
    <div class="contact">
      <p class="contact__name">Maren Dunleavy</p>
      <p class="contact__role">Director of Operations</p>
      <p class="contact__address">27 Ashbrook Lane<br>Middletown, MD. 21584</p>
      <p><span class="contact__label">Tel:</span>&nbsp; (313) 555-0147</p>
      <p><span class="contact__label">Fax:</span> (949) 555-0192</p>
      <p><span class="contact__label">Email:</span> maren@cmpaddocks.example</p>
      <p><span class="contact__label">Web:</span> cmpaddocks.example</p>
    </div>
  </article>

  <article class="card card--gold">
    <div class="brand">
      <span class="brand__dot"></span>
      <p class="brand__name">Crest of<br>Morning<br>Paddocks</p>
    </div>
    <span class="divider"></span>
    <div class="contact">
      <p class="contact__name">Maren Dunleavy</p>
      <p class="contact__role">Director of Operations</p>
      <p class="contact__address">27 Ashbrook Lane<br>Middletown, MD. 21584</p>
      <p><span class="contact__label">Tel:</span>&nbsp; (313) 555-0147</p>
      <p><span class="contact__label">Fax:</span> (949) 555-0192</p>
      <p><span class="contact__label">Email:</span> maren@cmpaddocks.example</p>
      <p><span class="contact__label">Web:</span> cmpaddocks.example</p>
    </div>
  </article>
</main>
</body>
</html>
```